Donations Website - Fund page design

We need an on brand fund page for our crowdfunding website. The design should keep in mind Quillmark Framegrid 3 default columns and spacing.

Please use this development site as a guide... ( under construction )
http://dario.fundquay.example:8080/

Elements to include:
• Framegrid 3 default column layout ( based on 12 column / 1140px / 30px gutters )
• Fund title ( Default Page Fund Title )
• Fund image / video ( 16:9 ratio )
• Fund progress: Current $ amount, Goal $ amount, # donations, # supporters, # views, % progress, progress bar, # shares
• Share buttons ( Chatterbook, Chirply, Vexlo+, WorkMesh, Clipboardy, Email )
• Donate button
• Sections for ( Fund story, fund updates and fund comments... could be tabbed )
• Section for recent donations (name + cb photo / icon + anonymous / donation amount, short message )
• Button to report this fund
• Fund created by section ( name, chatterbook photo if they've verified using chatterbook and number of friends )
• Contact fund raiser button/link
Updates

The design brief has been updated. I've attached the logo as well, please use unless you feel you have something better to include.

Thanks.

I can't stress enough that this is 'NOT' a home page design. This is a personal fund page for a single user. Please do not include 'Other funds' on this page to promote.

Thanks,

Dario

The page should be similar to these pages. As you can see, these are single fund pages within these sites. I do not want my page to look like these, but have the features I included in the brief while fitting my site's design.

http://www.pledgeorbit.example/4kq9zr
https://www.backerloft.example/projects/524190377/lumo-ridge?ref=home_location
http://www.fundhaven.example/projects/the-green-harborites

Thanks,

Dario

Target Market(s)

Adults age 18-50 mainly. Anyone that potentially needs to raise money.

Industry/Entity Type

Construction

Font styles to use
Sans Serif

Colors

Designer to choose colors to be used in the design.

Requirements
Must have
• • Framegrid 3 default column layout ( based on 12 column / 1140px / 30px gutters )
• Donate button
Nice to have
• Would be nice to keep in mind that users may be able to choose a theme color during fund setup. But if the design is strong enough on its own we will not include this option.

```html
<!DOCTYPE html>
<html lang="en">
<head>
<meta charset="utf-8">
<title>John Smith Support Page – Fundquay</title>
<link rel="stylesheet" href="https://fonts.googleapis.com/css2?family=Open+Sans:wght@300;400;600;700&family=Lobster&display=swap">
<style>
:root{
  --header:#2d2d2d;
  --page:#f4f4f4;
  --lower:#efefef;
  --ink:#2b3a42;
  --text:#777;
  --label:#666;
  --green:#3cc48f;
  --green-light:#4ccaa0;
  --orange:#f37b2b;
  --orange-btn:#fbb040;
  --teal:#80d0c7;
  --teal-line:#62c0b5;
  --teal-btn:#7fd4cb;
  --navy:#263540;
  --beige:#f1ede4;
  --white:#fff;
  --tab:#cfcfcf;
}
*{margin:0;padding:0;box-sizing:border-box}
html,body{width:810px;height:1200px;overflow:hidden}
body{position:relative;background:var(--page);font-family:"Open Sans",Arial,sans-serif;color:var(--text)}
.abs{position:absolute}

.site-header{position:absolute;left:0;top:0;width:810px;height:50px;background:var(--header)}
.brand{position:absolute;left:80px;top:14px;display:flex;align-items:center;gap:6px;color:var(--white);font-weight:700;font-size:15px;letter-spacing:.5px}
.brand-dot{width:18px;height:18px;border-radius:50%;background:var(--white)}
.main-nav{position:absolute;left:378px;top:19px;display:flex;font-size:9px;color:#ddd}
.main-nav span{padding:0 11px;border-left:1px solid #666;line-height:11px}
.main-nav span:first-child{border-left:0;padding-left:0}
.btn-head{position:absolute;top:11px;height:27px;border-radius:2px;color:var(--white);font-size:8.5px;font-weight:700;display:flex;align-items:center;justify-content:center}
.btn-signup{left:623px;width:50px;background:var(--orange-btn)}
.btn-login{left:679px;width:51px;background:var(--teal-btn)}

.page-title{position:absolute;left:78px;top:72px;font-size:24px;font-weight:400;color:var(--ink);letter-spacing:-.2px}

.card{position:absolute;background:var(--white);border:1px solid #e2e2e2;box-shadow:0 5px 5px -3px rgba(0,0,0,.18)}
.hero{left:78px;top:114px;width:381px;height:217px}
.hero-media{position:absolute;left:6px;top:6px;width:368px;height:204px;background:radial-gradient(ellipse at 55% 45%,#c99a7e 0%,#a87a5c 30%,#6f8a3a 62%,#3f5d1c 100%)}
.owner{left:478px;top:114px;width:253px;height:217px}
.owner-inner{position:absolute;left:6px;top:6px;width:241px;height:204px;background:var(--beige)}
.owner-photo{position:absolute;left:18px;top:22px;width:98px;height:99px;background:linear-gradient(160deg,#d8b48e,#9fc4e0)}
.owner-label{position:absolute;left:124px;top:26px;font-size:10px;color:#555}
.owner-name{position:absolute;left:124px;top:38px;font-size:12px;color:var(--green-light)}
.owner-friends{position:absolute;left:124px;top:63px;font-size:10px;color:#444;display:flex;align-items:center;gap:6px}
.owner-friends b{color:#333}
.btn-contact{position:absolute;left:122px;top:89px;width:111px;height:31px;background:var(--orange-btn);color:var(--white);font-size:8.5px;font-weight:700;display:flex;align-items:center;justify-content:center}
.btn-donate{position:absolute;left:12px;top:143px;width:215px;height:47px;background:var(--green);color:var(--white);font-size:17px;font-weight:700;letter-spacing:.6px;display:flex;align-items:center;justify-content:center;gap:10px}

.stat{position:absolute;top:354px}
.stat-label{font-size:10.5px;color:var(--label)}
.stat-value{font-size:14px;font-weight:600;color:#444;margin-top:3px}
.stat-value.money{color:var(--orange)}
.stat-value.goal{color:var(--green)}
.progress-label{position:absolute;left:502px;top:352px;font-size:10.5px;color:var(--label)}
.progress-label b{font-size:13px;color:#555}
.progress-bar{position:absolute;left:502px;top:377px;width:229px;height:8px;border-radius:4px;background:#fdc95a;overflow:hidden}
.progress-fill{width:90%;height:100%;background:#e79a2f}

.share-bar{position:absolute;left:78px;top:406px;width:653px;height:49px;background:var(--teal);border:1px solid var(--teal-line);border-radius:2px}
.share-cell{position:absolute;top:0;height:47px;border-left:1px solid var(--teal-line);display:flex;flex-direction:column;align-items:center;justify-content:center;gap:4px;color:var(--white)}
.share-total{left:0;width:78px;border-left:0}
.share-total b{font-size:22px;line-height:20px;color:#2b3a42;font-weight:700}
.share-total span{font-size:10px;font-weight:700}
.share-pill{background:var(--white);border-radius:2px;height:12px;padding:0 3px;display:flex;align-items:center;gap:2px;font-size:7px;color:#666}
.share-pill i{display:block;width:8px;height:8px;background:#8a9aa0;border-radius:1px}
.share-count{font-size:9.5px;font-weight:700}
.btn-report{position:absolute;left:481px;top:7px;width:164px;height:35px;background:var(--navy);color:var(--white);font-size:10.5px;font-weight:600;display:flex;align-items:center;justify-content:center;gap:24px}

.divider{position:absolute;left:0;top:508px;width:810px;height:692px;background:var(--lower);border-top:1px solid #d3d3d3}

.tab{position:absolute;top:562px;height:36px;font-size:9px;font-weight:700;color:#444;display:flex;align-items:center;justify-content:center;background:var(--tab)}
.tab.active{background:var(--white);height:38px;border:1px solid #e3e3e3;border-bottom:0}
.story{position:absolute;left:78px;top:597px;width:444px;height:521px;background:var(--white);border:1px solid #e3e3e3;border-top:0;box-shadow:0 5px 5px -3px rgba(0,0,0,.16)}
.story-title{position:absolute;left:24px;top:18px;font-family:"Lobster",cursive;font-size:16px;color:var(--orange)}
.story-media{position:absolute;left:21px;top:51px;width:178px;height:108px;border-radius:5px;background:#1b1b1b;padding:6px 7px}
.story-media div{width:100%;height:100%;background:linear-gradient(180deg,#f4f6f8,#e2e8ee)}
.story-body{position:absolute;left:20px;top:52px;width:402px;font-size:10.5px;line-height:15.2px;color:var(--text)}
.story-body .float{float:left;width:190px;height:126px}
.story-body b{color:#555}
.story-body u{color:#555}
.story-body h3{font-size:10.5px;color:var(--green);font-weight:600;margin-top:15px}

.donations-title{position:absolute;left:541px;top:548px;font-family:"Lobster",cursive;font-size:20px;color:var(--orange)}
.donations-sub{position:absolute;left:541px;top:573px;font-size:10px;color:#444}
.donation{position:absolute;left:541px;width:189px;height:134px;border-bottom:1px solid #d8d8d8}
.donor-photo{position:absolute;left:0;top:0;width:73px;height:60px;border:3px solid var(--white);box-shadow:0 1px 3px rgba(0,0,0,.2)}
.donor-name{position:absolute;left:82px;top:-2px;font-size:10px;font-weight:700;color:#444}
.donor-amount{position:absolute;left:81px;top:10px;font-size:32px;font-weight:300;color:var(--green-light);line-height:36px}
.donor-time{position:absolute;left:83px;top:50px;font-size:9px;color:#555}
.donor-note{position:absolute;left:21px;top:71px;width:170px;font-size:8.8px;line-height:13.6px;color:#444}
.donor-note::before{content:"\201C";position:absolute;left:-21px;top:-3px;font-size:22px;color:#555;font-weight:700}

.site-footer{position:absolute;left:0;top:1158px;width:810px;height:42px;background:var(--navy);color:var(--white);font-size:9px;display:flex;align-items:center;justify-content:center}
</style>
</head>
<body>

<header class="site-header">
  <div class="brand"><span class="brand-dot"></span>FUNDQUAY</div>
  <nav class="main-nav"><span>HOW IT WORKS</span><span>FAQS</span><span>SUPPORT</span><span>ABOUT</span></nav>
  <div class="btn-head btn-signup">SIGN UP</div>
  <div class="btn-head btn-login">LOGIN</div>
</header>

<h1 class="page-title">John Smith Support Page</h1>

<div class="card hero"><div class="hero-media" role="img" aria-label="Portrait photo of the fund beneficiary outdoors"></div></div>

<div class="card owner">
  <div class="owner-inner">
    <div class="owner-photo" role="img" aria-label="Profile photo of the fund creator"></div>
    <div class="owner-label">Fund Created by:</div>
    <div class="owner-name">James Wagon</div>
    <div class="owner-friends">
      <svg width="20" height="16" viewBox="0 0 20 16"><g fill="none" stroke="#9aa7c7" stroke-width="1.2"><circle cx="8" cy="5" r="3.2"/><path d="M2 15c0-4 3-5.5 6-5.5s6 1.5 6 5.5z"/><path d="M12 2.2a3 3 0 1 1 0 5.6M15 9.8c2 .6 3.5 2 3.5 5.2h-3"/></g></svg>
      Friends - <b>569</b>
    </div>
    <div class="btn-contact">Contact Fund Raiser</div>
    <div class="btn-donate">DONATE NOW
      <svg width="28" height="25" viewBox="0 0 28 25"><path d="M14 24S1 16 1 8a6.5 6.5 0 0 1 13-1.5A6.5 6.5 0 0 1 27 8c0 8-13 16-13 16z" fill="#fff"/></svg>
    </div>
  </div>
</div>

<div class="stat" style="left:79px"><div class="stat-label">Raised: <svg width="8" height="6" viewBox="0 0 8 6"><path d="M0 0h8L4 6z" fill="#e33"/></svg></div><div class="stat-value money">$45,000.00</div></div>
<div class="stat" style="left:184px"><div class="stat-label">Goal:</div><div class="stat-value goal">$50,000.00</div></div>
<div class="stat" style="left:280px"><div class="stat-label">Donations:</div><div class="stat-value">121</div></div>
<div class="stat" style="left:366px"><div class="stat-label">Support:</div><div class="stat-value">560</div></div>
<div class="stat" style="left:440px"><div class="stat-label">Views:</div><div class="stat-value">1560</div></div>
<div class="progress-label">Fund Progress: <b>90%</b></div>
<div class="progress-bar"><div class="progress-fill"></div></div>

<div class="share-bar">
  <div class="share-cell share-total"><b>389</b><span>Shares</span></div>
  <div class="share-cell" style="left:78px;width:64px"><div class="share-pill"><i></i>Share</div><div class="share-count">307</div></div>
  <div class="share-cell" style="left:142px;width:66px"><div class="share-pill"><i></i>Share</div><div class="share-count">14</div></div>
  <div class="share-cell" style="left:208px;width:64px"><div class="share-pill"><i></i>Share</div><div class="share-count">3</div></div>
  <div class="share-cell" style="left:272px;width:67px"><div class="share-pill"><i></i>Share</div><div class="share-count">65</div></div>
  <div class="share-cell" style="left:339px;width:66px"><div class="share-pill"><i></i>Share</div><div class="share-count">0</div></div>
  <div class="share-cell" style="left:405px;width:66px"><div class="share-pill"><i></i>Email</div><div class="share-count">0</div></div>
  <div class="btn-report">Report this Fund
    <svg width="17" height="17" viewBox="0 0 17 17"><circle cx="8.5" cy="8.5" r="8.5" fill="#fff"/><rect x="7.3" y="3.5" width="2.4" height="6.5" rx="1" fill="#263540"/><circle cx="8.5" cy="12.5" r="1.3" fill="#263540"/></svg>
  </div>
</div>

<div class="divider"></div>

<div class="tab active" style="left:78px;width:100px">Fund Story</div>
<div class="tab" style="left:179px;width:99px">Fund Updates</div>
<div class="tab" style="left:280px;width:99px">Fund Comments</div>

<section class="story">
  <h2 class="story-title">lorem ipsum dolor sit amet</h2>
  <div class="story-media"><div role="img" aria-label="Tablet showing a project dashboard with charts"></div></div>
  <div class="story-body">
    <div class="float"></div>
    <p>Sed quis nisi euismod, fermentum tellus a, lobortis quam. Vestibulum condimentum mi vitae diam tristique, egestas dignissim diam mattis. Curabitur vel diam in massa porttitor dictum id in lorem. <u>Vivamus faucibus</u> ac leo ac dignissim. Maecenas orci est, euismod facilisis feugiat sit amet, semper ut tortor. Donec eleifend accumsan nisl, nec laoreet leo iaculis sit amet. <b>Vivamus varius</b> arcu eu hendrerit. Vivamus eu magna rhoncus, consectetur metus ac, varius lacus. Donec ultricies, tortor quis sagittis sagittis, mauris erat ullamcorper augue, eu placerat diam nunc a lorem.</p>
    <h3>Nam vulputate mauris id arcu pharetra</h3>
    <p>Sed posuere quam cursus. Nullam eget massa vel mi posuere venenatis sed quis tortor. In hac habitasse platea dictumst. Fusce nisi tellus, fermentum a luctus eget, convallis vitae orci. In commodo egestas magna quis placerat. Quisque adipiscing consequat nisi, nec accumsan quam venenatis ac.</p>
    <h3>Fusce quam dui, accumsan a magna in</h3>
    <p>Nullam eget massa vel mi posuere venenatis sed quis tortor. In hac habitasse platea dictumst. Fusce nisi tellus, fermentum a luctus eget, convallis vitae orci. In commodo egestas magna quis placerat.</p>
    <h3>Nam vulputate mauris id arcu pharetra</h3>
    <p>Sed posuere quam cursus. Nullam eget massa vel mi posuere venenatis sed quis tortor. In hac habitasse platea dictumst. Fusce nisi tellus, fermentum a luctus eget, convallis vitae orci. In commodo egestas magna quis placerat. Quisque adipiscing consequat nisi, nec accumsan quam venenatis ac.</p>
  </div>
</section>

<h2 class="donations-title">Recent Donations (234)</h2>
<div class="donations-sub">$45,000.00 raised in 12 days</div>

<div class="donation" style="top:598px">
  <div class="donor-photo" role="img" aria-label="Donor profile photo" style="background:linear-gradient(160deg,#e8c9a8,#b98a66)"></div>
  <div class="donor-name">Steve Williams</div><div class="donor-amount">$150</div><div class="donor-time">25 mins ago</div>
  <p class="donor-note">Lorem ipsum dolor sit amet, consectetur adipiscing elit. Sed quis nisi euismod, fermentum tellus a, lobortis quam.</p>
</div>
<div class="donation" style="top:732px">
  <div class="donor-photo" role="img" aria-label="Donor profile photo" style="background:linear-gradient(160deg,#9aa54a,#d6a98a)"></div>
  <div class="donor-name">Tom Carpenter</div><div class="donor-amount">$160</div><div class="donor-time">2 hours ago</div>
  <p class="donor-note">Donec eleifend accumsan nisl, nec laoreet leo iaculis sit amet. Vivamus varius arcu eu sagittis aliquam.</p>
</div>
<div class="donation" style="top:866px">
  <div class="donor-photo" role="img" aria-label="Donor profile photo" style="background:linear-gradient(160deg,#7f9a3e,#d9a57c)"></div>
  <div class="donor-name">John Smith</div><div class="donor-amount">$250</div><div class="donor-time">2 days ago</div>
  <p class="donor-note">Vivamus varius arcu eu sagittis aliquam. Donec eleifend accumsan nisl, nec laoreet leo iaculis sit amet.</p>
</div>
<div class="donation" style="top:1000px">
  <div class="donor-photo" role="img" aria-label="Donor profile photo" style="background:linear-gradient(160deg,#3a2a22,#a8765a)"></div>
  <div class="donor-name">Rose Hans</div><div class="donor-amount">$100</div><div class="donor-time">2 days ago</div>
  <p class="donor-note">Vivamus varius arcu eu sagittis aliquam. Donec eleifend accumsan nisl, nec laoreet leo iaculis sit amet.</p>
</div>

<footer class="site-footer">© 2014 Fundquay. All rights reserved.</footer>

</body>
</html>
```